Redesign of Business Card to look more professional and stand out

Business card design. You can lean more about our company by going to dkrfabworks.example. Raised letters would be nice. Company name & Address
DK&R
418 Wendlow Ridge Drive, Suite 340
Calder Springs, OH 44871

You can use my name and title: Glenn Harwick
Business Development Manager

Target Market(s)

Heavy Industrial market, i.e. utilities, chemical plants, paper mills, construction companies

Industry/Entity Type

Construction

Contact Information for Business Card

We provide Project Management & Project Support Services

Font styles to use
Serif

Requirements
Must have
• Company name & Address
• DK&R
• 418 Wendlow Ridge Drive, Suite 340
• Calder Springs, OH 44871
Nice to have
• ideas for the back of the card
Should not have
• no crazy colors. needs to look professional and standout.

```html
<!DOCTYPE html>
<html lang="en">
<head>
<meta charset="utf-8">
<title>DK&amp;R Business Card</title>
<link rel="stylesheet" href="https://fonts.googleapis.com/css2?family=Tinos:wght@400;700&display=swap">
<style>
  :root {
    --navy: #1d3566;
    --white: #ffffff;
    --accent: #c4531f;
    --backdrop: #2d2b2c;
  }
  html, body {
    margin: 0;
    width: 1200px;
    height: 900px;
    overflow: hidden;
    background: var(--backdrop);
    font-family: "Tinos", "Times New Roman", serif;
  }
  .sheet {
    width: 1200px;
    height: 900px;
    display: flex;
    flex-direction: column;
    align-items: center;
    justify-content: center;
    gap: 56px;
  }
  .card {
    width: 640px;
    height: 366px;
    display: block;
    box-shadow: 0 10px 28px rgba(0,0,0,0.45);
  }
  .wordmark { font-weight: 700; letter-spacing: 1px; }
  .name { font-weight: 700; font-size: 22px; fill: var(--white); }
  .title { font-size: 13.5px; fill: var(--white); }
  .contact { font-size: 15px; fill: var(--white); }
  .address { font-size: 17px; fill: var(--white); }
</style>
</head>
<body>
<main class="sheet">

  <svg class="card card-front" viewBox="0 0 640 366" role="group" aria-label="Business card front">
    <rect width="640" height="366" fill="var(--white)"/>
    <path class="navy-band" d="M0 172 L282 172 L316 132 Q325 122 338 122 L640 122 L640 366 L0 366 Z" fill="var(--navy)"/>
    <line class="accent-rule" x1="0" y1="172" x2="640" y2="172" stroke="var(--accent)" stroke-width="3"/>

    <text class="wordmark" x="48" y="104" font-size="66" fill="var(--navy)">DK&amp;R</text>

    <text class="name" x="350" y="146">Glenn Harwick</text>
    <text class="title" x="352" y="164">Business Development Manager</text>

    <g class="contact-list">
      <g class="icon-phone" transform="translate(48 207)" fill="var(--white)">
        <path d="M1 3 Q6 0 11 3 L10 6 L8 5 Q6 4.5 4 5 L2 6 Z"/>
        <rect x="2" y="7" width="8" height="5" rx="1"/>
      </g>
      <text class="contact" x="72" y="219">555-204-0148</text>

      <g class="icon-mail" transform="translate(48 233)">
        <rect x="0" y="0" width="12" height="9" fill="var(--white)"/>
        <path d="M0 0 L6 5 L12 0" fill="none" stroke="var(--navy)" stroke-width="1.2"/>
      </g>
      <text class="contact" x="72" y="244">info@dkrfabworks.example</text>

      <g class="icon-link" transform="translate(48 257)" fill="none" stroke="var(--white)" stroke-width="1.6">
        <rect x="0" y="4" width="7" height="4" rx="2"/>
        <rect x="5" y="2" width="7" height="4" rx="2"/>
      </g>
      <text class="contact" x="72" y="269">www.dkrfabworks.example</text>
    </g>

    <g class="address-block">
      <path class="icon-home" d="M330 222 L338 215 L346 222 L344 222 L344 229 L340 229 L340 225 L336 225 L336 229 L332 229 L332 222 Z" fill="var(--white)"/>
      <text class="address" x="356" y="229">DK&amp;R</text>
      <text class="address" x="330" y="262">418 Wendlow Ridge Drive,</text>
      <text class="address" x="330" y="290">Suite 340 Calder Springs, OH 44871</text>
    </g>
  </svg>

  <svg class="card card-back" viewBox="0 0 640 366" role="group" aria-label="Business card back">
    <rect width="640" height="366" fill="var(--navy)"/>
    <text class="wordmark" x="320" y="207" font-size="96" fill="var(--white)" text-anchor="middle">DK&amp;R</text>
  </svg>

</main>
</body>
</html>
```